Existing WP site needs a fresh look (design only)

The current website, www.tarnbelle.com.au, is fine, but needs a fresh look so their clients can tell their website has been 'refreshed' regularly.
https://www.tarnbelle.com.au/sitemap/
They will use the existing functionality.
They want to keep the blue, green and white of their logo as the main colors, but a fresh look. They prefer a light look to a dark look, but they would be open to good designs that change their mind.
Be creative, think outside the box.
You only need to supply the 'home page ' design to win but the winners will be asked to provide an extra 'standard' page template (like the one currently being used for search results and other pages)
Any photos used must be supplied without charge with the PSDs in a resolution acceptable for the WordPress site.
2 page

```html
<!DOCTYPE html>
<html lang="en">
<head>
<meta charset="utf-8">
<title>Tarnbelle – Home</title>
<link href="https://fonts.googleapis.com/css2?family=Roboto:wght@400;500&display=swap" rel="stylesheet">
<style>
:root{
  --green:#7dbf2a;
  --green-soft:#e5f0d5;
  --ink:#1a1a1a;
  --muted:#6b6b6b;
  --teal:#25a98a;
  --teal-soft:#d8f1e8;
  --line:#9cc96a;
  --card-line:#ececec;
  --circle:#4a66ad;
  --snap:#b0085c;
  --chirp:#26a9e1;
  --work:#0a74b8;
}
*{box-sizing:border-box;margin:0;padding:0}
html,body{width:704px;height:1200px;overflow:hidden;background:#fff}
body{position:relative;font-family:'Roboto',sans-serif;color:var(--ink)}
.abs{position:absolute}
.logo-box{left:0;top:0;width:139px;height:59px;background:var(--green-soft);border-bottom-right-radius:8px}
.brand{font-weight:500;color:#fff;font-size:15px;display:flex;align-items:center;gap:5px}
.brand .dot{width:10px;height:10px;background:var(--green)}
.hero-panel{left:533px;top:0;width:171px;height:323px;background:var(--green-soft)}
.nav{left:223px;top:22px;display:flex;align-items:center;font-size:10px;gap:0}
.nav a{color:var(--ink);text-decoration:none;padding:3px 6px}
.nav span{color:#777;font-size:9px}
.nav a.active{color:var(--green);border:1px solid var(--line);background:#eef6e3;border-radius:3px}
.hero-title{left:52px;top:121px;font-size:25px;line-height:29px;font-weight:500}
.hero-title em{font-style:normal;color:var(--green)}
.hero-text{left:52px;top:194px;width:300px;font-size:9.5px;line-height:11.6px;color:var(--muted)}
.btn-soft{background:var(--teal-soft);color:var(--teal);border:1px solid #9fdcc6;border-radius:3px;font-size:10px;display:flex;align-items:center;justify-content:center}
.hero-btn{left:52px;top:261px;width:67px;height:22px}
.hero-mic{left:483px;top:81px;width:157px;height:242px;border-radius:40px 40px 20px 20px;background:linear-gradient(160deg,#555 0%,#2f2f2f 45%,#8bc43a 60%,#3a3a3a 75%)}
.partners{left:0;top:341px;width:704px;height:55px;background:var(--green-soft);display:flex;align-items:center;justify-content:space-between;padding:0 52px;color:#fff;font-size:11px;font-weight:500}
.search-mic{left:74px;top:432px;width:76px;height:142px;border-radius:30px 30px 6px 6px;background:linear-gradient(180deg,var(--green) 0%,var(--green) 65%,#37474f 100%)}
.field{border:1px solid var(--line);border-radius:3px;height:22px;font-size:9.5px;color:#999;display:flex;align-items:center;justify-content:space-between;padding:0 6px;background:#fff}
.search-input{left:237px;top:426px;width:415px}
.or{left:237px;top:465px;width:415px;text-align:center;font-size:9.5px}
.select{width:129px}
.search-btn{left:237px;top:558px;width:415px;height:22px;background:var(--green);color:#fff;font-size:10px;border-radius:3px;display:flex;align-items:center;justify-content:center}
.wave{left:52px;top:621px;width:600px;height:98px;background:linear-gradient(180deg,#fff 0%,#d0d0d0 30%,#8a8a8a 50%,#d0d0d0 70%,#fff 100%)}
.sec-head{display:flex;align-items:center;gap:6px}
.sec-icon{width:11px;height:32px;border:2px solid var(--teal);border-radius:6px 6px 3px 3px}
.sec-head h2{font-size:16px;font-weight:400;line-height:15px}
.sec-head small{display:block;color:#aaa;font-size:9.5px}
.card{border:1px solid var(--card-line);border-radius:3px;background:#fff;box-shadow:0 1px 3px rgba(0,0,0,.04)}
.artist{left:52px;width:296px;height:103px}
.artist .photo{left:8px;top:7px;width:87px;height:87px;border-radius:5px;background:linear-gradient(135deg,#cfcfcf,#3a3a3a)}
.artist h3{left:107px;top:10px;font-size:10px;font-weight:400}
.artist .role{left:107px;top:25px;font-size:6px;color:var(--teal)}
.artist p{left:107px;top:41px;width:165px;font-size:5.6px;line-height:7px;color:#555}
.artist .demo{left:107px;top:75px;width:76px;height:17px;font-size:8px;gap:6px}
.play{width:10px;height:10px;border:1px solid var(--teal);border-radius:50%}
.news{left:355px;width:297px;height:66px}
.news .photo{left:6px;top:5px;width:55px;height:55px;background:linear-gradient(135deg,#bbb,#333)}
.news h3{left:71px;top:6px;font-size:9.5px;font-weight:400}
.news .date{left:71px;top:21px;font-size:5.6px;color:var(--teal);display:flex;gap:3px;align-items:center}
.news .date i{width:6px;height:6px;border:1px solid var(--teal);display:block}
.news p{left:71px;top:32px;width:165px;font-size:5.5px;line-height:7px;color:#666}
.social{top:1027px;width:136px;height:29px;color:#fff;font-size:12px;display:flex;align-items:center;padding-left:10px;gap:24px}
.social i{width:18px;height:18px;border:2px solid #fff;border-radius:4px;display:block}
.footer{left:0;top:1078px;width:704px;height:122px;background:var(--green-soft)}
.foot-brand{left:52px;top:1112px;font-size:22px}
.foot-brand .dot{width:18px;height:18px}
.foot-info{font-size:9.5px;line-height:11.5px;display:flex;gap:6px}
.copy{left:0;top:1173px;width:704px;text-align:center;font-size:9.5px}
</style>
</head>
<body>
<div class="abs logo-box"></div>
<div class="abs brand" style="left:52px;top:22px"><span class="dot"></span>Tarnbelle</div>
<div class="abs hero-panel"></div>
<nav class="abs nav">
  <a class="active">VOICES</a><span>|</span><a>RATES</a><span>|</span><a>PAYMENTS</a><span>|</span><a>NEWS</a><span>|</span><a>ABOUT US</a><span>|</span><a>CONTACT</a><span>|</span><a>SHORTLIST</a>
</nav>
<h1 class="abs hero-title">Australia's Top <em>Voices</em><br>Professional Casting</h1>
<p class="abs hero-text">Lorem ipsum dolor sit amet, consectetur adipiscing elit, sed do eiusmod tempor incididunt ut labore et dolore magna aliqua. Quis ipsum suspendisse ultrices gravida. Risus commodo viverra maecenas accumsan lacus vel facilisis.</p>
<div class="abs btn-soft hero-btn">See More</div>
<div class="abs hero-mic" role="img" aria-label="Illustration of a studio microphone with green accents"></div>

<div class="abs partners">
  <span>Harbourline</span><span>Tenmile</span><span>Bluegate</span><span>Northwave Media</span><span>Channel Kite</span><span>Skyfield</span><span>Fieldplay</span><span>Strand</span><span>Orbitfm</span>
</div>

<div class="abs search-mic" role="img" aria-label="Illustration of a green microphone"></div>
<div class="abs field search-input">Search artists ....
  <svg width="12" height="12" viewBox="0 0 12 12"><circle cx="5" cy="5" r="4" fill="none" stroke="#999"/><line x1="8" y1="8" x2="11" y2="11" stroke="#999"/></svg></div>
<div class="abs or">OR</div>
<div class="abs field select" style="left:237px;top:492px">Location<svg width="9" height="5"><path d="M0 0 4.5 4.5 9 0" fill="none" stroke="#999"/></svg></div>
<div class="abs field select" style="left:380px;top:492px">Sex<svg width="9" height="5"><path d="M0 0 4.5 4.5 9 0" fill="none" stroke="#999"/></svg></div>
<div class="abs field select" style="left:524px;top:492px">Age Range<svg width="9" height="5"><path d="M0 0 4.5 4.5 9 0" fill="none" stroke="#999"/></svg></div>
<div class="abs field select" style="left:237px;top:525px">Talent Range<svg width="9" height="5"><path d="M0 0 4.5 4.5 9 0" fill="none" stroke="#999"/></svg></div>
<div class="abs field select" style="left:380px;top:525px">Language<svg width="9" height="5"><path d="M0 0 4.5 4.5 9 0" fill="none" stroke="#999"/></svg></div>
<div class="abs field select" style="left:524px;top:525px">Accent<svg width="9" height="5"><path d="M0 0 4.5 4.5 9 0" fill="none" stroke="#999"/></svg></div>
<div class="abs search-btn">Search</div>

<div class="abs wave" role="img" aria-label="Grey audio waveform decoration"></div>

<div class="abs sec-head" style="left:52px;top:748px"><i class="sec-icon"></i><h2>Spotlight<small>Artists</small></h2></div>
<div class="abs sec-head" style="left:356px;top:748px"><i class="sec-icon"></i><h2>News<small>Latest</small></h2></div>

<article class="abs card artist" style="top:795px">
  <div class="abs photo" role="img" aria-label="Black and white portrait of a voice artist"></div>
  <h3 class="abs">Marcus Pellow</h3><span class="abs role">Artist - Melbourne</span>
  <p class="abs">Malleable, fast, efficient and easy to work with, Marcus likes to say that he's a director's dream, but he also likes to say that self-recomm</p>
  <div class="abs btn-soft demo"><i class="play"></i>2021 Demo</div>
</article>
<article class="abs card artist" style="top:905px">
  <div class="abs photo" role="img" aria-label="Black and white portrait of a voice artist"></div>
  <h3 class="abs">Marcus Pellow</h3><span class="abs role">Artist - Melbourne</span>
  <p class="abs">Malleable, fast, efficient and easy to work with, Marcus likes to say that he's a director's dream, but he also likes to say that self-recomm</p>
  <div class="abs btn-soft demo"><i class="play"></i>2021 Demo</div>
</article>

<article class="abs card news" style="top:795px">
  <div class="abs photo" role="img" aria-label="Portrait photo of a featured voice artist"></div>
  <h3 class="abs">NEW VOICE ALERT | Owen Hartley</h3><span class="abs date"><i></i>8 Aug 2021</span>
  <p class="abs">Lorem ipsum dolor sit amet, consectetur adipiscing elit, sed do eiusmod tempor incididunt ut labore et dolore magna aliqua. Quis ipsum suspendisse ultrices gravida.</p>
</article>
<article class="abs card news" style="top:869px">
  <div class="abs photo" role="img" aria-label="Portrait photo of a featured voice artist"></div>
  <h3 class="abs">NEW VOICE ALERT | Owen Hartley</h3><span class="abs date"><i></i>8 Aug 2021</span>
  <p class="abs">Lorem ipsum dolor sit amet, consectetur adipiscing elit, sed do eiusmod tempor incididunt ut labore et dolore magna aliqua. Quis ipsum suspendisse ultrices gravida.</p>
</article>
<article class="abs card news" style="top:942px">
  <div class="abs photo" role="img" aria-label="Portrait photo of a featured voice artist"></div>
  <h3 class="abs">NEW VOICE ALERT | Owen Hartley</h3><span class="abs date"><i></i>8 Aug 2021</span>
  <p class="abs">Lorem ipsum dolor sit amet, consectetur adipiscing elit, sed do eiusmod tempor incididunt ut labore et dolore magna aliqua. Quis ipsum suspendisse ultrices gravida.</p>
</article>

<a class="abs social" style="left:52px;background:var(--circle)"><i></i>Circlebook</a>
<a class="abs social" style="left:206px;background:var(--snap)"><i></i>Snapframe</a>
<a class="abs social" style="left:361px;background:var(--chirp)"><i></i>Chirpline</a>
<a class="abs social" style="left:515px;background:var(--work)"><i></i>Worknet</a>

<footer class="abs footer"></footer>
<div class="abs brand foot-brand"><span class="dot"></span>Tarnbelle</div>
<div class="abs foot-info" style="left:274px;top:1103px">
  <svg width="16" height="24" viewBox="0 0 16 24"><path d="M8 0a8 8 0 0 0-8 8c0 6 8 16 8 16s8-10 8-16a8 8 0 0 0-8-8z" fill="#111"/><circle cx="8" cy="8" r="3" fill="#e5f0d5"/></svg>
  <div>Tarnbelle Pty Limited<br>Suite 14, 90 Wattle Lane Kelsey Park<br>NSW 2099 Australia</div>
</div>
<div class="abs foot-info" style="left:491px;top:1103px">
  <svg width="14" height="24" viewBox="0 0 14 24"><rect x="1" y="1" width="12" height="22" rx="2" fill="none" stroke="#111" stroke-width="2"/><line x1="1" y1="18" x2="13" y2="18" stroke="#111"/></svg>
  <div>SYDNEY:+ 61 2 5550 1420<br>MELBOURNE:+ 61 3 5550 2368</div>
</div>
<p class="abs copy">© Copyright 2018 Tarnbelle Pty Limited. Privacy Policy &amp; Terms and Conditions</p>
</body>
</html>
```